Education Certificate

We need a modern yet professional Certificate for those who successfully pass / complete our online Training course.

There are various courses but ONE certificate design required.

the certificate needs to look extremely professional and of value.

```html
<!DOCTYPE html>
<html lang="en">
<head>
<meta charset="utf-8">
<title>Certificate of Recognition</title>
<link rel="stylesheet" href="https://fonts.googleapis.com/css2?family=Outfit:wght@400;500;700&family=Montserrat:wght@700;800&family=Open+Sans:wght@300;400;600&display=swap">
<style>
  :root {
    --ink: #2d2d2d;
    --ink-soft: #555555;
    --paper: #ffffff;
    --red-bright: #cc0000;
    --red-deep: #850000;
    --gold-dark: #c97b2e;
    --gold-light: #f9e89c;
    --gold-warm: #d8902a;
    --sign-area: #f2f2f2;
  }
  html, body {
    margin: 0;
    padding: 0;
    width: 1200px;
    height: 901px;
    overflow: hidden;
    background: var(--paper);
  }
  .canvas {
    position: relative;
    width: 1200px;
    height: 901px;
  }
  .sheet {
    position: absolute;
    left: 69px;
    top: 80px;
    width: 1026px;
    height: 726px;
    background: var(--paper);
    box-shadow: 0 18px 60px rgba(0, 0, 0, 0.16);
  }
  .frame {
    position: absolute;
    left: 0;
    top: 0;
    width: 1200px;
    height: 901px;
  }
  .corner-art {
    position: absolute;
  }
  .corner-art--left {
    left: 69px;
    top: 214px;
    width: 192px;
    height: 592px;
    clip-path: polygon(0 0, 58% 30%, 100% 100%, 0 100%);
    background: linear-gradient(160deg, var(--gold-warm) 0%, var(--red-deep) 35%, var(--red-bright) 75%, var(--gold-warm) 100%);
  }
  .corner-art--right {
    left: 916px;
    top: 80px;
    width: 179px;
    height: 558px;
    clip-path: polygon(0 0, 100% 0, 100% 100%, 42% 70%, 42% 24%);
    background: linear-gradient(200deg, var(--red-bright) 0%, var(--red-deep) 55%, var(--gold-warm) 100%);
  }
  .content {
    position: absolute;
    left: 322px;
    width: 600px;
    margin: 0;
    text-align: center;
    color: var(--ink);
    line-height: 1;
  }
  .title {
    top: 287px;
    font-family: "Outfit", sans-serif;
    font-weight: 500;
    font-size: 28px;
    letter-spacing: 2px;
  }
  .awarded-to {
    top: 328px;
    font-family: "Open Sans", sans-serif;
    font-weight: 600;
    font-size: 11.5px;
    letter-spacing: 3.6px;
  }
  .recipient {
    top: 362px;
    left: 272px;
    width: 700px;
    font-family: "Outfit", sans-serif;
    font-weight: 700;
    font-size: 60px;
    letter-spacing: -0.5px;
  }
  .completion {
    top: 452px;
    font-family: "Open Sans", sans-serif;
    font-weight: 600;
    font-size: 12px;
    letter-spacing: 1px;
  }
  .course {
    top: 490px;
    font-family: "Montserrat", sans-serif;
    font-weight: 800;
    font-size: 20px;
    letter-spacing: 5.6px;
  }
  .description {
    top: 533px;
    font-family: "Open Sans", sans-serif;
    font-weight: 300;
    font-size: 11px;
    line-height: 16.5px;
    color: var(--ink-soft);
  }
  .issued-label {
    top: 579px;
    font-family: "Open Sans", sans-serif;
    font-weight: 600;
    font-size: 12px;
    letter-spacing: 0.8px;
  }
  .issue-date {
    position: absolute;
    left: 551px;
    top: 607px;
    width: 143px;
    height: 24px;
    border-bottom: 1.5px solid var(--ink);
    display: flex;
    justify-content: space-around;
    align-items: center;
    font-family: "Open Sans", sans-serif;
    font-size: 8.5px;
    letter-spacing: 0.6px;
    color: var(--ink);
  }
  .issue-date .divider {
    display: inline-block;
    width: 1px;
    height: 17px;
    background: var(--ink);
    transform: rotate(30deg);
  }
  .signatory {
    position: absolute;
    top: 605px;
    width: 223px;
    text-align: center;
  }
  .signatory--director { left: 291px; }
  .signatory--student { left: 731px; }
  .signature {
    display: block;
    height: 56px;
    margin: 0 22px 7px;
    background: var(--sign-area);
    border-radius: 4px;
  }
  .signatory--student .signature {
    margin: -24px 50px 7px 60px;
    height: 80px;
  }
  .sign-line {
    border-top: 1.5px solid var(--ink);
    padding-top: 7px;
    font-family: "Outfit", sans-serif;
    font-weight: 500;
    font-size: 10px;
    letter-spacing: 1.6px;
    color: var(--ink);
    white-space: nowrap;
  }
</style>
</head>
<body>
<main class="canvas">
  <div class="sheet"></div>

  <svg class="frame" viewBox="0 0 1200 901" aria-hidden="true">
    <defs>
      <linearGradient id="gold-frame" x1="0" y1="0" x2="1" y2="0">
        <stop offset="0" stop-color="#c97b2e"/>
        <stop offset="0.4" stop-color="#f9e89c"/>
        <stop offset="1" stop-color="#d8902a"/>
      </linearGradient>
    </defs>
    <rect x="100" y="111" width="965" height="665" fill="none" stroke="url(#gold-frame)" stroke-width="7.5"/>
  </svg>

  <div class="corner-art corner-art--left" role="img" aria-label="Red and gold geometric corner decoration"></div>
  <div class="corner-art corner-art--right" role="img" aria-label="Red and gold geometric corner decoration"></div>

  <h1 class="content title">CERTIFICATE OF RECOGNITION</h1>
  <p class="content awarded-to">THIS CERTIFICATED IS AWARED TO</p>
  <h2 class="content recipient">Thomas Ashby Carter</h2>
  <p class="content completion">For the successful completion of the online course:</p>
  <p class="content course">LOREM ONLINE WORKSHOP</p>
  <p class="content description">Lorem ipsum dolor sit amet proud, consectetuer adipiscing elit, lorem diam<br>nonummy nibh euismod of tincidunt ut laoreet dolore magna aliquam erat volutpat.</p>
  <p class="content issued-label">Issued on:</p>

  <div class="issue-date">
    <span>30</span><span class="divider"></span><span>September</span><span class="divider"></span><span>2020</span>
  </div>

  <div class="signatory signatory--director">
    <span class="signature" role="img" aria-label="Handwritten signature of the director"></span>
    <div class="sign-line">HELEN R. MARSH, DIRECTOR</div>
  </div>

  <div class="signatory signatory--student">
    <span class="signature" role="img" aria-label="Handwritten signature of the student"></span>
    <div class="sign-line">CLARA VOSS WHITMORE, STUDENT</div>
  </div>
</main>
</body>
</html>
```